Mobile Repair Service on location needs a Web Design

We are starting a new mobile device repair service called Gadget Haven and our website needs a design!

Hello Designers!
First, we'd like to make clear this is more than a simple web design contest, we want the designers to create an idea. We want someone who can create the whole theme of the service's we provide. We want someone that can help design our visual branding, help us communicate a sentiment. And we are willing to pay for that.

Who are we?
Our company is based in Rotterdam, the Netherlands. We provide different services for all kinds of electronic devices. The kind of services we provide are, among other things, installations of hardware and software and the repair of broken or malfunctioning devices.
We are starting a new service that offers mobile device repairs on location, be it at the home of our customers, their office, or any other place. Just give us the address and we will come to you for the repair job. This is also our main USP. We have multiple skilled engineers who drive trough the country on a daily basis and can be on location within a working day. Repair is done immediately onsite while the customer waits. At this stage we will start with the smartphone product-group within the mobile devices. In a second phase we might also add tablets.
People don't want to be without their phone for weeks because of some parts that needed to be ordered by a repair center they had to sent their phone to. We offer a fully functional mobile repair center in the form of specially customized vans. These vans have all the tools and utilities needed by our engineers to safely repair your mobile device. Your phone is being repaired directly in front of you, the next business-day, on a location you desire.

For this new service we are creating a website called Gadget Haven. The website needs a story and matching design and this is where you come in. We are not looking for a simple template design we can get from any place. We need a story. We want you to create an idea, build a unique theme or vision that helps sell the product/service. This goes beyond the design of the website. We need the whole package, the design you are creating needs to have returning elements like icons, color use, images, maybe even characters etc. You name it! There needs to be a common thread in the design so we can reuse elements in, for example, the email templates, the work order or receipt we give to our customers (we may contact the winner of the contest to design these for us as well!).

The name 'Gadget Haven' is chosen. Haven (short for rehabilitate) has a bold and playful tone to it and the design needs to reflect the name. So we're looking for a somewhat playful and cheeky design. Definitely not too serious and definitely modern. We already got a logo that we love and that fit's this description (see attached design documents for the logo). It's bold, powerful and fun. Our web design needs to reflect this as well and has to fit in with our logo.
We would really like it if the design somehow incorporates elements that highlight our unique selling points (repairs on location, we come to you etc.). We would really like some form of story telling in the design. Think clumsy people breaking their phones. Teenagers in tears because they have no access to their friends. People nowadays have the need to always be 'connected'. What happens when your phone is broken or malfunctioning? We're handling tech, we are nerds and a little bit weird, but we're professionals and here to help you with your problem. The sentiment Wire Troop tries to communicate is something we really like. We're looking for fresh idea's, anything goes!

In an overview all Unique Selling Points of the Gadget haven service:
- Professional service on location. Don’t ship to us we will come to you!
- Clear pricing upfront. No hidden cost.
- Next business-day repair.
- Backed by a professional call center open 12 hours a day and open on a Saturday as well
- Backed by a professional repair center with more then 12 years of experience
- Repair is done by certified engineers
- 1 year warranty on the repair

The process:
The main function of our website will be for customers to make a repair request. A customer will visit our website and can make a repair request immediately by going through a 'request-order-flow'. In this flow he or she will need to fill in some forms and can select wich type/model/brand of mobile device he or she has and what parts need to be repaired. After a request is placed we will call the customer back (within an hour) for a short intake and to set a date/time and location. Our engineer will meet the customer at the specified location and will repair the device onsite in one of our mobile repair centers, which is a specialized van equipped with all the tools needed for device restorations.
So in short the steps are:
- Choose your device and repair job
- Place the order
- Get a callback within the hour
- Set date and location
- We will come to you.

Website functionality:
Our website is our main form of communication. So the sentiment we want to communicate needs be reflected in the design. We need a main/front page designed (preferably a long scrolling page design) containing:
1. Customers will be able to request a repair job directly on our website. So there will need to be a prominent button/link at the top of our main page that will bring the customer to this 'request-order-flow'. This is the main flow which needs to be full focus on the front page. All other items are secondary.
2. The general information of who we are and what we do, and why the customer should choose us. Preferably in short bullet-point type keywords/sentences with icons or other visual cues. See our unique selling points to get an idea of the information that will be displayed here.
3. There needs to be a section that will explain the process (see above) of a repair request step-by- step, again in brief short key sentences and with (custom) icons.
4. There needs to be a section that explains to the customer he/she can always contact us if they are not sure what the problem is with their device, and for this reason are not sure what repair request they should order.
5. We want to implement some functionality that display customer ratings or customer reviews. So there needs to be room for some kind of widget of plugin we're going to implement which shows these reviews.
6. A 'For business section' where we will explain all the options we provide for corporate clients.
7. Social media links.
8. There needs to be a menu with buttons that leads to the all sections described in the previous points.

For now, we need a design for our front page. In the second phase, when we have picked our winner, we may ask the winner to design the page(s) for our request workflow as well.

EDIT:
Finally, we have a very specific order in mind for the different segments of our website. We would like you to add some more segments that were not in our original brief as well:

1. Top header with order/request button. (should instantly make clear our main USP, we do repairs on location)
2. Our process
3. Our unique selling points / why choose us
4. The kind of repairs we do (broken screens, broken batteries, water damage, broken camera's, no sound etc.)
5. A 'meet our team' section, where we introduce some of our engineers
6. A 'contact us for any questions' section/
7. Testimonials/user reviews
8. A section where we show key performance indicators
9. 'For businesses' sections
10.'Subscribe for newsletter' field
11. Social media buttons

Industry/Entity Type

It Service

Number of Pages Required

1 page

Font styles to use
Sans Serif

Requirements
Must have
• a main/front page, design only
• custom icons/images for banners, adverts online and in print (high res)
Nice to have
• Storytelling in our design.
• Design that fits with our brand new logo.
• Elements like icons to have a flat design.
• Keep in mind that the website will need to be responsive when designing! (Ideally provide an example of the mobile design as well)
• Create a fun and trustworthy feeling.

```html
<!DOCTYPE html>
<html lang="en">
<head>
<meta charset="utf-8">
<title>Gadget Haven – Mobile Repair On Location</title>
<link href="https://fonts.googleapis.com/css2?family=Montserrat:wght@400;600;700;800&family=Open+Sans:wght@400;600;700&display=swap" rel="stylesheet">
<style>
:root{
  --orange:#f26522;
  --yellow:#f6b92e;
  --purple:#716c91;
  --dark:#2a2a2a;
  --darker:#1d1d1d;
  --green:#8dc63f;
  --light:#ececec;
  --text:#666;
  --white:#fff;
}
*{box-sizing:border-box;margin:0;padding:0}
html,body{width:1200px;height:3432px;overflow:hidden}
body{font-family:"Open Sans",Arial,sans-serif;color:var(--text);font-size:13px;line-height:1.6;background:var(--white)}
h1,h2,h3,h4,.nav a,.btn{font-family:"Montserrat",Arial,sans-serif}
section,header,footer{position:relative;width:1200px;overflow:hidden}
.btn{display:inline-block;font-size:12px;font-weight:700;text-transform:uppercase;letter-spacing:.5px;padding:12px 22px;text-decoration:none}
.btn-dark{background:var(--dark);color:var(--white)}
.btn-orange{background:var(--orange);color:var(--white)}
.section-title{text-align:center;font-size:34px;font-weight:800;color:var(--dark);text-transform:uppercase;letter-spacing:1px}
.lead{text-align:center;width:920px;margin:14px auto 0;font-size:12.5px}

/* hero */
.hero{height:620px;background:var(--light)}
.hero-art{position:absolute;left:0;top:0;width:1200px;height:540px;background:linear-gradient(180deg,#e9e9e9 0%,#dcdcdc 100%)}
.hero-art .hands{position:absolute;left:140px;top:30px;width:920px;height:510px;border-radius:8px;background:radial-gradient(ellipse at 50% 60%,#f3c7a4 0%,#e7b08a 35%,rgba(220,220,220,0) 72%)}
.brand{position:absolute;left:40px;top:28px;display:flex;align-items:center;gap:12px}
.brand .dot{width:46px;height:46px;border-radius:50%;background:var(--orange)}
.brand span{font-family:"Montserrat",sans-serif;font-weight:800;font-size:26px;color:var(--dark);letter-spacing:.5px}
.nav{position:absolute;right:40px;top:36px;display:flex;gap:4px}
.nav a{font-size:11px;font-weight:700;color:var(--dark);text-decoration:none;padding:9px 12px;text-transform:uppercase}
.nav a.active{background:var(--white);border:1px solid #ccc}
.cta-bar{position:absolute;left:300px;top:540px;width:700px;height:80px;background:var(--dark);display:flex;align-items:center}
.cta-bar .icon{width:110px;height:80px;background:var(--green);display:flex;align-items:center;justify-content:center}
.cta-bar .copy{flex:1;padding:0 20px}
.cta-bar h3{color:var(--white);font-size:17px;font-weight:700;text-transform:uppercase}
.cta-bar p{color:#aaa;font-size:10.5px;line-height:1.4}
.cta-bar .btn{margin-right:20px;padding:10px 16px;font-size:11px}

/* welcome */
.welcome{height:420px;padding-top:50px}
.features{display:grid;grid-template-columns:repeat(3,300px);column-gap:40px;row-gap:30px;width:980px;margin:40px auto 0}
.feature{display:flex;gap:12px}
.feature svg{flex:none}
.feature h4{font-size:13px;font-weight:600;color:var(--dark);margin-bottom:4px}
.feature p{font-size:11px;line-height:1.5}

/* who we are */
.who{height:610px;background:var(--yellow);padding-top:40px}
.who .section-title{color:var(--dark)}
.who .tagline{text-align:center;color:var(--white);font-size:16px;font-weight:600}
.who .lead{color:#5a4a1e;margin-top:6px}
.who-art{position:absolute;left:70px;top:210px;width:640px;height:380px;background:linear-gradient(135deg,#f3b12a 0%,#3a3a3a 50%,#1f1f1f 100%);border-radius:6px}
.who-text{position:absolute;left:760px;top:220px;width:380px}
.who-text h3{font-size:20px;font-weight:700;color:var(--dark);margin-bottom:8px}
.who-text p{color:#5a4a1e;font-size:12px;margin-bottom:26px}

/* process */
.process{height:520px;padding-top:50px}
.steps{position:relative;width:980px;margin:50px auto 0;height:300px}
.step{position:absolute;width:370px}
.step h4{font-size:13px;font-weight:700;color:var(--dark);text-transform:uppercase;margin-bottom:6px}
.step p{font-size:11px}
.step .more{font-family:"Montserrat",sans-serif;color:var(--orange);font-weight:700;font-size:10px;text-transform:uppercase}
.step.left{left:0;text-align:right}
.step.right{left:610px}
.num{position:absolute;width:96px;height:96px;border-radius:50%;background:var(--orange);color:var(--white);font-family:"Montserrat",sans-serif;font-size:32px;font-weight:700;display:flex;align-items:center;justify-content:center;border:5px solid #f7a27a}

/* testimonials */
.testimonials{height:200px;background:var(--purple);display:flex;align-items:center;padding:0 80px}
.testimonials h2{color:var(--white);font-size:48px;font-weight:800;letter-spacing:1px;width:520px;display:flex;align-items:center;gap:16px}
.testimonials blockquote{color:#e4e2ee;font-size:12.5px;font-style:italic;width:520px}
.testimonials cite{display:flex;align-items:center;gap:10px;margin-top:12px;font-style:normal;font-size:11px;color:var(--white)}
.testimonials cite i{width:34px;height:34px;border-radius:50%;background:#9a96b5;display:block}

/* why */
.why{height:520px;padding:40px 80px}
.why h2{font-size:24px;font-weight:400;color:var(--text);text-transform:uppercase;line-height:1.1}
.why h2 strong{display:block;font-size:44px;font-weight:800;color:var(--dark)}
.why p{width:560px;margin-top:20px;font-size:12.5px}
.why .btn{margin-top:24px;background:var(--white);color:var(--dark);border:2px solid var(--dark)}
.why-art{position:absolute;left:700px;top:30px;width:420px;height:450px;border-radius:50%;background:radial-gradient(circle at 50% 45%,#f5f5f5 0%,#d6dde4 60%,#b9c3cc 100%)}

/* quote */
.quote{height:310px;background:var(--dark)}
.quote-art{position:absolute;left:0;top:0;width:480px;height:310px;background:linear-gradient(135deg,#f4f4f4,#dcdcdc);clip-path:polygon(0 0,86% 0,100% 100%,0 100%)}
.quote-art .pin{position:absolute;left:150px;top:70px;width:150px;height:170px;border-radius:50%;background:var(--orange);opacity:.85}
.quote-form{position:absolute;left:540px;top:40px;width:600px}
.quote-form h2{color:var(--white);font-size:26px;font-weight:700;margin-bottom:18px}
.fields{display:grid;grid-template-columns:1fr 1fr;gap:12px 20px}
.field label{display:block;color:#bbb;font-size:11px;margin-bottom:4px}
.field .box{height:30px;background:var(--white)}
.quote-form .btn{margin-top:18px;background:var(--white);color:var(--dark);padding:9px 18px;font-size:11px;border-radius:16px}

/* contact */
.contact{height:170px;background:#f2f2f2;display:flex;justify-content:space-between;padding:38px 120px 0}
.contact-item{display:flex;gap:14px;width:300px}
.contact-item .ic{width:46px;height:46px;background:var(--purple);display:flex;align-items:center;justify-content:center;flex:none}
.contact-item h4{font-size:16px;font-weight:700;color:var(--dark)}
.contact-item p{font-size:11.5px}

/* footer */
.footer{height:62px;background:var(--darker);display:flex;align-items:center;justify-content:space-between;padding:0 80px}
.footer nav a{color:#999;font-size:10.5px;text-decoration:none;text-transform:uppercase;margin-right:14px}
.footer small{display:block;color:#666;font-size:9.5px}
.social{display:flex;gap:8px}
.social i{width:26px;height:26px;border-radius:50%;background:#555;display:block}
</style>
</head>
<body>

<header class="hero">
  <div class="hero-art"><div class="hands" role="img" aria-label="Illustration of raised hands holding smartphones with broken screens and repair icons"></div></div>
  <div class="brand"><div class="dot"></div><span>GADGET HAVEN</span></div>
  <nav class="nav">
    <a class="active" href="#">Home</a><a href="#">About us</a><a href="#">Services</a><a href="#">Repair</a><a href="#">Blog</a><a href="#">Contact us</a>
  </nav>
  <div class="cta-bar">
    <div class="icon"><svg width="44" height="44" viewBox="0 0 44 44" fill="none" stroke="#fff" stroke-width="3"><circle cx="22" cy="22" r="9"/><path d="M22 4v8M22 32v8M4 22h8M32 22h8"/></svg></div>
    <div class="copy">
      <h3>Do you need a mobile repair?</h3>
      <p>Our engineers come to your home, office or any place you choose and fix your phone on the spot.</p>
    </div>
    <a class="btn btn-orange" href="#">Request a quote</a>
  </div>
</header>

<section class="welcome">
  <h2 class="section-title">Welcome to Gadget Haven</h2>
  <p class="lead">We repair smartphones right where you are. Tell us what is wrong, pick a time and place, and one of our engineers drives to you in a fully equipped repair van. Your phone is fixed in front of you while you wait, with clear pricing up front and no hidden costs. No shipping, no weeks without your phone, just quick and friendly help from people who love tech.</p>
  <div class="features">
    <div class="feature"><svg width="34" height="34" viewBox="0 0 34 34" fill="none" stroke="#444" stroke-width="2"><path d="M17 3a10 10 0 0 1 10 10c0 8-10 18-10 18S7 21 7 13A10 10 0 0 1 17 3z"/><circle cx="17" cy="13" r="3.5"/></svg><div><h4>Professional service on location</h4><p>Don't ship your phone to us, we will come to you wherever you are.</p></div></div>
    <div class="feature"><svg width="34" height="34" viewBox="0 0 34 34" fill="none" stroke="#444" stroke-width="2"><path d="M4 18 18 4h12v12L16 30z"/><circle cx="24" cy="10" r="2"/></svg><div><h4>Clear pricing upfront</h4><p>You know the price before we start. No hidden costs, ever.</p></div></div>
    <div class="feature"><svg width="34" height="34" viewBox="0 0 34 34" fill="none" stroke="#444" stroke-width="2"><circle cx="17" cy="17" r="13"/><path d="M17 9v8l6 4"/></svg><div><h4>Next business day repair</h4><p>Our engineers reach you within one working day, anywhere in the country.</p></div></div>
    <div class="feature"><svg width="34" height="34" viewBox="0 0 34 34" fill="none" stroke="#444" stroke-width="2"><path d="M6 28 20 14M18 6a7 7 0 0 0 10 10l-4-4z"/></svg><div><h4>Backed by a professional</h4><p>A repair centre with more than twelve years of experience behind every job.</p></div></div>
    <div class="feature"><svg width="34" height="34" viewBox="0 0 34 34" fill="none" stroke="#444" stroke-width="2"><circle cx="17" cy="14" r="9"/><path d="M12 22l-3 9 8-4 8 4-3-9"/></svg><div><h4>Repair is done by certified engineers</h4><p>Trained, certified and friendly experts handle your device with care.</p></div></div>
    <div class="feature"><svg width="34" height="34" viewBox="0 0 34 34" fill="none" stroke="#444" stroke-width="2"><path d="M17 3 29 8v9c0 7-5 12-12 14C10 29 5 24 5 17V8z"/><path d="m11 17 4 4 8-8"/></svg><div><h4>1 year warranty on the repair</h4><p>Every repair comes with a full year of warranty for your peace of mind.</p></div></div>
  </div>
</section>

<section class="who">
  <h2 class="section-title">Who we are</h2>
  <p class="tagline">Tech nerds on wheels</p>
  <p class="lead">We are a team of curious, slightly weird and very professional engineers. We fix broken screens, tired batteries and soaked phones, and we do it right in front of you.</p>
  <div class="who-art" role="img" aria-label="Photo of a smartphone with a shattered screen, glass fragments flying off"></div>
  <div class="who-text">
    <h3>What we do</h3>
    <p>We repair smartphones on location from our mobile repair vans. Screens, batteries, cameras, speakers and water damage are fixed on the spot while you wait, so you are never disconnected for long.</p>
    <h3>Our Stories</h3>
    <p>Dropped in the canal, sat on by the dog, or simply tired after years of use. Every phone has a story, and we love helping our customers write a happy ending to it.</p>
    <a class="btn btn-dark" href="#">Read more</a>
  </div>
</section>

<section class="process">
  <h2 class="section-title">The Process</h2>
  <p class="lead">Requesting a repair takes only a few minutes. Choose your device and what needs fixing, place your order and we will call you back within the hour to plan a date, time and location. Then we come to you and repair your phone on the spot.</p>
  <div class="steps">
    <div class="step left" style="top:0"><h4>Choose your device and repair job</h4><p>Select the brand, model and the parts that need repair in our simple request form.</p><span class="more">Read more</span></div>
    <div class="step right" style="top:0"><h4>Place the order</h4><p>Check the clear upfront price and confirm your repair request in one click.</p><span class="more">Read more</span></div>
    <div class="step left" style="top:170px"><h4>Get a callback within the hour</h4><p>One of our staff calls you for a short intake to check every detail.</p><span class="more">Read more</span></div>
    <div class="step right" style="top:170px"><h4>Set date and location</h4><p>Pick the moment and place that suits you, and our engineer will be there.</p><span class="more">Read more</span></div>
    <div class="num" style="left:385px;top:0">01</div>
    <div class="num" style="left:500px;top:0">02</div>
    <div class="num" style="left:385px;top:170px">03</div>
    <div class="num" style="left:500px;top:170px">04</div>
  </div>
</section>

<section class="testimonials">
  <h2><svg width="56" height="56" viewBox="0 0 56 56" fill="#fff"><path d="M6 12h44v26H22l-10 10V38H6z"/></svg>TESTIMONIALS</h2>
  <div>
    <blockquote>"My screen cracked on a Monday and by Tuesday lunchtime it was fixed in front of my office. Friendly engineer, fair price and no stress at all. I would recommend them to anyone."</blockquote>
    <cite><i></i>Happy customer</cite>
  </div>
</section>

<section class="why">
  <h2>Why the customer<strong>should choose us?</strong></h2>
  <p>Because your phone is your connection to everything. We know how it feels to be without it, so we make repairs fast, easy and honest. Our engineers come to you the next business day, fix your device on the spot with quality parts and give you a full year of warranty. Our call centre is open twelve hours a day and on Saturdays too, so help is always close by.</p>
  <p>Not sure what is wrong with your device? Just contact us and we will help you find the right repair, without any obligation.</p>
  <a class="btn" href="#">Read more</a>
  <div class="why-art" role="img" aria-label="Illustration of a friendly repair engineer mascot in blue overalls holding a wrench"></div>
</section>

<section class="quote">
  <div class="quote-art" role="img" aria-label="Illustration of a location pin with a repair symbol"><div class="pin"></div></div>
  <div class="quote-form">
    <h2>Request a Quote</h2>
    <div class="fields">
      <div class="field"><label>Name</label><div class="box"></div></div>
      <div class="field"><label>Email</label><div class="box"></div></div>
      <div class="field"><label>Phone</label><div class="box"></div></div>
      <div class="field"><label>Device</label><div class="box"></div></div>
    </div>
    <a class="btn" href="#">Submit</a>
  </div>
</section>

<section class="contact">
  <div class="contact-item"><div class="ic"><svg width="22" height="22" viewBox="0 0 22 22" fill="#fff"><path d="M11 1a7 7 0 0 1 7 7c0 5-7 13-7 13S4 13 4 8a7 7 0 0 1 7-7zm0 4a3 3 0 1 0 0 6 3 3 0 0 0 0-6z"/></svg></div><div><h4>Address</h4><p>14 Havenkade, 3011 AB<br>Rotterdam, the Netherlands</p></div></div>
  <div class="contact-item"><div class="ic"><svg width="22" height="22" viewBox="0 0 22 22" fill="#fff"><path d="M5 2h4l2 5-3 2a12 12 0 0 0 5 5l2-3 5 2v4c0 1-1 2-2 2A17 17 0 0 1 3 4c0-1 1-2 2-2z"/></svg></div><div><h4>Tel</h4><p>Local: +31 10 555 0142<br>Mobile: +31 10 555 0178</p></div></div>
  <div class="contact-item"><div class="ic"><svg width="22" height="22" viewBox="0 0 22 22" fill="none" stroke="#fff" stroke-width="2"><rect x="2" y="5" width="18" height="13"/><path d="m2 5 9 7 9-7"/></svg></div><div><h4>Email</h4><p>hello@gadgethaven.example<br>care@gadgethaven.example</p></div></div>
</section>

<footer class="footer">
  <div>
    <nav><a href="#">Home</a><a href="#">About us</a><a href="#">Services</a><a href="#">Repair</a><a href="#">Blog</a><a href="#">Contact us</a></nav>
    <small>Copyright © Gadget Haven. All rights reserved.</small>
  </div>
  <div class="social"><i></i><i></i><i></i><i></i></div>
</footer>

</body>
</html>
```